KV HOLDWELL GROUP LETTERHEAD

I need letterhead for "KV Holdwell group LLC" ...

logo attached to project...

Company Info:
845 North Marlow Avenue, Suite 7B
Chicago, Illinois 60611
ofc 312-555-0184
facsimile 312-555-0172
www.kvholdwellgroup.example
info@kvholdwellgroup.example

I have multiple projects listed.. see below:

Business cards for ashford lane equity llc
letterhead
envelopes

Business cards for KV Holdwell LLC
letterhead
envelopes

```html
<!DOCTYPE html>
<html lang="en">
<head>
<meta charset="utf-8">
<title>KV Holdwell Group LLC — Letterhead</title>
<link rel="stylesheet" href="https://fonts.googleapis.com/css2?family=Cinzel:wght@500&family=Josefin+Sans:wght@400&display=swap">
<style>
  :root {
    --header-bg: #b9cad8;
    --ink-navy: #1f4c7c;
    --ink-deep: #0f3f70;
    --band-end: #86a4bf;
    --paper: #ffffff;
  }
  html, body {
    margin: 0;
    padding: 0;
    overflow: hidden;
  }
  body {
    width: 924px;
    height: 1200px;
    background: var(--paper);
  }
  .letterhead {
    position: relative;
    width: 924px;
    height: 1200px;
    background: var(--paper);
    overflow: hidden;
  }
  .masthead {
    position: absolute;
    left: 0;
    top: 0;
    width: 924px;
    height: 233px;
    background: var(--header-bg);
  }
  .brand-mark {
    position: absolute;
    left: 66px;
    top: 60px;
    width: 336px;
    text-align: center;
  }
  .brand-mark__dot {
    display: block;
    width: 72px;
    height: 72px;
    margin: 0 auto 18px;
    border-radius: 50%;
    background: var(--ink-navy);
  }
  .brand-mark__name {
    font-family: "Cinzel", serif;
    font-weight: 500;
    font-size: 27px;
    color: var(--ink-navy);
    letter-spacing: 0.5px;
    white-space: nowrap;
  }
  .contact {
    position: absolute;
    right: 48px;
    top: 32px;
    text-align: right;
  }
  .contact__company {
    font-family: "Cinzel", serif;
    font-weight: 500;
    font-size: 15px;
    color: var(--ink-navy);
    margin: 0 22px 12px 0;
    letter-spacing: 0.4px;
  }
  .contact__company small {
    font-size: 9px;
  }
  .contact__list {
    list-style: none;
    margin: 0;
    padding: 0;
  }
  .contact__item {
    font-family: "Josefin Sans", sans-serif;
    font-size: 16px;
    line-height: 22.5px;
    color: var(--ink-deep);
    display: flex;
    justify-content: flex-end;
    align-items: center;
    gap: 10px;
  }
  .contact__item::after {
    content: "";
    width: 8px;
    height: 8px;
    background: var(--ink-deep);
    flex: none;
    margin-top: -3px;
  }
  .footer-band {
    position: absolute;
    left: 0;
    top: 1067px;
    width: 924px;
    height: 56px;
    background: linear-gradient(90deg, var(--ink-deep) 0%, #3f6c98 45%, var(--band-end) 100%);
  }
  .footer-band__name {
    position: absolute;
    left: 21px;
    top: 11px;
    margin: 0;
    font-family: "Cinzel", serif;
    font-weight: 500;
    font-size: 28px;
    color: var(--paper);
    letter-spacing: 0.5px;
    white-space: nowrap;
  }
  .footer-band__name small {
    font-size: 18px;
  }
</style>
</head>
<body>
  <div class="letterhead">
    <header class="masthead">
      <div class="brand-mark">
        <span class="brand-mark__dot"></span>
        <div class="brand-mark__name">KV HOLDWELL GROUP LLC</div>
      </div>
      <address class="contact">
        <div class="contact__company">KV HOLDWELL GROUP <small>LLC</small></div>
        <ul class="contact__list">
          <li class="contact__item">845 North Marlow Avenue, Suite 7B</li>
          <li class="contact__item">Chicago, Illinois 60611</li>
          <li class="contact__item">ofc 312-555-0184</li>
          <li class="contact__item">facsimile 312-555-0172</li>
          <li class="contact__item">www.kvholdwellgroup.example</li>
          <li class="contact__item">info@kvholdwellgroup.example</li>
        </ul>
      </address>
    </header>
    <footer class="footer-band">
      <p class="footer-band__name">KV HOLDWELL GROUP <small>LLC</small></p>
    </footer>
  </div>
</body>
</html>
```